Looking for a clean, modern, and professional business card design that reflects Valtrim Systems

The design should include the company logo, contact details, and align with our brand identity. Please use a sophisticated and minimalist style, incorporating [specific colors, if applicable]. Creativity is welcome, but the card must maintain a polished and professional appearance.

Details to Include:

Name: Gavin Trelowe
Title: VP Sales / Operations
Company: Valtrim Systems
Phone: 483.216.7705
Email: gavin@valtrimsystems-example.com
Website: www.valtrimsystems-example.com

```html
<!DOCTYPE html>
<html lang="en">
<head>
<meta charset="utf-8">
<title>Valtrim Systems – Business Card</title>
<link rel="stylesheet" href="https://fonts.googleapis.com/css2?family=Montserrat:wght@500;700&family=Roboto:wght@400;700&display=swap">
<style>
  :root {
    --page: #e9eaec;
    --brand-blue: #3570b0;
    --brand-navy: #1b2f66;
    --ink: #1a1a1a;
    --text-grey: #4a4a4a;
    --divider: #b9b9b9;
    --card-white: #ffffff;
  }
  * { box-sizing: border-box; margin: 0; padding: 0; }
  html, body { width: 1200px; height: 874px; overflow: hidden; }
  body {
    background: var(--page);
    font-family: "Roboto", Arial, sans-serif;
    display: flex;
    flex-direction: column;
    align-items: center;
    justify-content: center;
    gap: 40px;
  }
  .card {
    width: 630px;
    height: 360px;
    border-radius: 22px;
    position: relative;
    overflow: hidden;
    box-shadow: 0 6px 18px rgba(0,0,0,0.18);
  }

  /* Front */
  .card--front {
    background: var(--brand-blue);
    display: flex;
    align-items: center;
    justify-content: center;
  }
  .wordmark {
    display: flex;
    align-items: center;
    gap: 14px;
    font-family: "Montserrat", Arial, sans-serif;
    font-weight: 700;
    letter-spacing: 0.02em;
    white-space: nowrap;
  }
  .wordmark__square { display: block; background: currentColor; }
  .card--front .wordmark { color: var(--brand-navy); font-size: 46px; }
  .card--front .wordmark__square { width: 30px; height: 30px; }

  /* Back */
  .card--back { background: var(--card-white); }
  .card--back .wordmark {
    position: absolute;
    left: 40px;
    top: 140px;
    color: var(--ink);
    font-size: 27px;
    gap: 10px;
  }
  .card--back .wordmark__square { width: 18px; height: 18px; }
  .divider {
    position: absolute;
    left: 322px;
    top: 110px;
    width: 2px;
    height: 140px;
    background: linear-gradient(var(--card-white), var(--divider) 30%, var(--divider) 70%, var(--card-white));
  }
  .contact {
    position: absolute;
    left: 342px;
    top: 118px;
  }
  .contact__name {
    color: var(--brand-blue);
    font-weight: 700;
    font-size: 27px;
    line-height: 1.1;
  }
  .contact__title {
    color: var(--ink);
    font-size: 16px;
    margin-top: 2px;
  }
  .contact__list { list-style: none; margin-top: 16px; }
  .contact__item {
    display: flex;
    align-items: center;
    gap: 8px;
    color: var(--text-grey);
    font-size: 16px;
    line-height: 1.4;
    white-space: nowrap;
  }
  .contact__icon { width: 13px; height: 13px; fill: var(--brand-blue); flex: none; }
  .footer-band {
    position: absolute;
    left: 0; right: 0; bottom: 0;
    height: 34px;
    border-top: 4px solid var(--ink);
    box-shadow: 0 -4px 0 var(--card-white);
    background: var(--brand-blue);
  }
</style>
</head>
<body>
  <section class="card card--front" aria-label="Card front">
    <div class="wordmark"><span class="wordmark__square"></span>Valtrim Systems</div>
  </section>

  <section class="card card--back" aria-label="Card back">
    <div class="wordmark"><span class="wordmark__square"></span>Valtrim Systems</div>
    <div class="divider"></div>
    <div class="contact">
      <p class="contact__name">Gavin Trelowe</p>
      <p class="contact__title">VP Sales / Operations</p>
      <ul class="contact__list">
        <li class="contact__item">
          <svg class="contact__icon" viewBox="0 0 24 24" aria-hidden="true"><path d="M6.6 10.8a15.1 15.1 0 0 0 6.6 6.6l2.2-2.2c.3-.3.7-.4 1-.2 1.1.4 2.3.6 3.6.6.6 0 1 .4 1 1V20c0 .6-.4 1-1 1C10.6 21 3 13.4 3 4c0-.6.4-1 1-1h3.5c.6 0 1 .4 1 1 0 1.3.2 2.5.6 3.6.1.3 0 .7-.2 1z"/></svg>
          483.216.7705
        </li>
        <li class="contact__item">
          <svg class="contact__icon" viewBox="0 0 24 24" aria-hidden="true"><path d="M2 5h20v14H2zm2 2v.5l8 5 8-5V7zm0 2.8V17h16V9.8l-8 5z"/></svg>
          gavin@valtrimsystems-example.com
        </li>
        <li class="contact__item">
          <svg class="contact__icon" viewBox="0 0 24 24" aria-hidden="true"><circle cx="12" cy="12" r="10"/></svg>
          www.valtrimsystems-example.com
        </li>
      </ul>
    </div>
    <div class="footer-band"></div>
  </section>
</body>
</html>
```